Business Card Design.

Life and Wellness Coach
www.brightpathwell.net
Want to use my name as the logo it could be the initials TRK or my full name. I want to trade mark me.
I like clean lines and simple designs, but it pops using the colors scheme (one or two colors) on the website.
I provide life and health coaching virtually and in person. My services include: Dietary Signal Screening, Sensitivity Clearing Review, Wellness Coaching, Life Coaching. Life and Health Assessments, and I sell foundational health products and specialized nutrition. Use colors that represent healing and trust.
Target Market(s)
Women for the ages of 30 - 60
Industry/Entity Type
Health
Contact Information for Business Card
Tessa Rosalind Kimble
Life and Wellness Coach
tessa@coachtrk.net
www.brightpathwell.net
555-217-8364
Health is not an event it's a lifestyle (tag line or if you have a better tag line)

```html
<!DOCTYPE html>
<html lang="en">
<head>
<meta charset="utf-8">
<title>Tessa Rosalind Kimble — Business Card</title>
<link href="https://fonts.googleapis.com/css2?family=Noto+Serif:ital,wght@0,400;0,500;1,400&display=swap" rel="stylesheet">
<style>
  :root {
    --sky-deep: #2f93f5;
    --sky-mid: #3fb4fb;
    --sky-light: #7fcdfd;
    --mint-light: #d3f8ec;
    --mint: #97f1da;
    --leaf: #5df52e;
    --sun: #f7f700;
    --ink: #1a1a1a;
    --white: #ffffff;
  }
  html, body {
    margin: 0;
    padding: 0;
    width: 1200px;
    height: 713px;
    overflow: hidden;
    background: #ffffff;
  }
  .card {
    position: relative;
    width: 1200px;
    height: 713px;
    overflow: hidden;
    font-family: "Noto Serif", Georgia, serif;
  }
  .card-art {
    position: absolute;
    inset: 0;
  }
  .identity {
    position: absolute;
    left: 417px;
    top: 222px;
    margin: 0;
  }
  .name {
    margin: 0;
    font-style: italic;
    font-weight: 400;
    font-size: 42px;
    letter-spacing: 1px;
    color: var(--ink);
    line-height: 1;
  }
  .role {
    margin: 12px 0 0 3px;
    font-style: italic;
    font-size: 34px;
    letter-spacing: 1px;
    color: var(--white);
    line-height: 1;
  }
  .contact {
    position: absolute;
    left: 490px;
    top: 340px;
    margin: 0;
    padding: 0;
    list-style: none;
    font-style: italic;
    font-size: 33px;
    letter-spacing: 1px;
    color: var(--ink);
  }
  .contact li {
    line-height: 56px;
    height: 56px;
  }
  .tagline {
    position: absolute;
    left: 0;
    right: 0;
    top: 657px;
    margin: 0;
    text-align: center;
    font-size: 33px;
    font-weight: 500;
    letter-spacing: 1px;
    color: var(--white);
    line-height: 1;
  }
</style>
</head>
<body>
<main class="card">
  <svg class="card-art" width="1200" height="713" viewBox="0 0 1200 713" aria-hidden="false">
    <defs>
      <linearGradient id="sky" x1="0" y1="1" x2="1" y2="0">
        <stop offset="0" stop-color="var(--sky-deep)"/>
        <stop offset="0.35" stop-color="var(--sky-light)"/>
        <stop offset="0.7" stop-color="var(--sky-mid)"/>
        <stop offset="1" stop-color="var(--sky-deep)"/>
      </linearGradient>
      <linearGradient id="mint" x1="0" y1="0" x2="1" y2="0">
        <stop offset="0" stop-color="var(--mint-light)"/>
        <stop offset="1" stop-color="var(--mint)"/>
      </linearGradient>
    </defs>
    <rect class="sky-backdrop" width="1200" height="713" fill="url(#sky)"/>
    <!-- mint swoosh band -->
    <path class="swoosh-band" d="M0,46 C420,48 900,150 1200,330 L1200,648 C700,642 300,520 0,398 Z" fill="url(#mint)"/>
    <!-- upper accent stripes -->
    <path class="stripe-leaf" d="M0,42 C420,44 900,146 1200,312 L1200,324 C900,156 420,52 0,50 Z" fill="var(--leaf)"/>
    <path class="stripe-sun" d="M0,50 C420,52 900,156 1200,324 L1200,340 C900,168 420,60 0,56 Z" fill="var(--sun)"/>
    <!-- lower accent stripe -->
    <path class="stripe-leaf-lower" d="M0,398 C300,520 700,642 1200,648 L1200,654 C700,652 300,536 0,420 Z" fill="var(--leaf)"/>
    <!-- figure mark area -->
    <ellipse class="figure-mark" cx="208" cy="284" rx="130" ry="140" fill="var(--white)" opacity="0.55"
             role="img" aria-label="Stylised white figure of a person leaping with arms outstretched"/>
  </svg>

  <header class="identity">
    <h1 class="name">Tessa Rosalind Kimble</h1>
    <p class="role">Life and Wellness Coach</p>
  </header>

  <ul class="contact">
    <li class="contact-phone">555-217-8364</li>
    <li class="contact-email">tessa@coachtrk.net</li>
    <li class="contact-web">www.brightpathwell.net</li>
  </ul>

  <p class="tagline">HEALTH IS NOT AN EVENT IT'S A LIFESTYLE</p>
</main>
</body>
</html>
```